Halvorsen Construction Needs a Business Card

Our current business card is very bland, and since we have a new logo, we would like a new business card design to reflect our company. It can be a single-sided or two-sided card, but it is important that our contact information appears on the same side. I am attaching a copy of our old card and our new logo. If you need the logo in another format than the one I'm sending, please let me know. This is the information that we must have on our card, but not necessarily in any specific order:
1) Our logo
2) General Contractor
3) Dale Halvorsen, Owner
4) 482 Commerce Ridge Road, Centre, Alabama 35871
5) Office: 256-555-0147
7) Fax: 256-555-0148
8) Cell: 256-555-0193
9) halvorsenconstruction@qvl-mail.net
10) halvorsenconstruction-example.com (can be omitted if necessary)
Also, I will need files in a format that I can alter if any of the above information changes in the near future. Thank you in advance for your submissions!
Target Market(s)
Commercial and residential clients, architects, and subcontractors.
Industry/Entity Type
Business
Look and feel

```html
<!DOCTYPE html>
<html lang="en">
<head>
<meta charset="utf-8">
<title>Halvorsen Construction – Business Card</title>
<link rel="stylesheet" href="https://fonts.googleapis.com/css2?family=Exo+2:wght@400;500;800&display=swap">
<style>
  :root {
    --page-bg: #e6e4e1;
    --card-white: #ffffff;
    --panel-dark: #333333;
    --accent-yellow: #f6b931;
    --ink-dark: #2b2b2b;
    --ink-light: #ffffff;
  }
  html, body {
    margin: 0;
    width: 1200px;
    height: 899px;
    overflow: hidden;
    background: var(--page-bg);
    font-family: "Exo 2", sans-serif;
  }
  .business-card {
    position: absolute;
    left: 140px;
    top: 180px;
    width: 920px;
    height: 540px;
    background: var(--card-white);
    border-radius: 44px;
    overflow: hidden;
    box-shadow: 0 10px 30px rgba(0,0,0,0.18);
  }
  .card-shapes { position: absolute; inset: 0; }
  .brand {
    position: absolute;
    left: 58px;
    top: 150px;
    display: flex;
    align-items: center;
    gap: 18px;
    color: var(--ink-dark);
    font-weight: 800;
  }
  .brand-square {
    width: 86px;
    height: 86px;
    background: var(--ink-dark);
  }
  .brand-name { line-height: 1; text-transform: uppercase; }
  .brand-name .word-main { display: block; font-size: 54px; letter-spacing: 1px; }
  .brand-name .word-sub { display: block; font-size: 22px; letter-spacing: 9px; margin-top: 4px; }
  .person {
    position: absolute;
    left: 72px;
    top: 318px;
  }
  .person-name {
    margin: 0;
    font-size: 22px;
    font-weight: 500;
    letter-spacing: 1px;
    color: var(--accent-yellow);
    text-transform: uppercase;
  }
  .person-title {
    margin: 4px 0 0;
    font-size: 16px;
    color: var(--ink-dark);
  }
  .address {
    position: absolute;
    left: 72px;
    top: 410px;
    font-style: normal;
    font-size: 20px;
    line-height: 1.45;
    color: var(--ink-dark);
  }
  .contact-list {
    position: absolute;
    right: 40px;
    top: 150px;
    margin: 0;
    padding: 0;
    list-style: none;
    color: var(--ink-light);
    font-size: 17px;
    text-align: right;
  }
  .contact-list li {
    display: flex;
    justify-content: flex-end;
    align-items: center;
    gap: 12px;
    height: 32px;
  }
  .contact-icon { width: 18px; height: 18px; flex: none; }
</style>
</head>
<body>
  <div class="business-card">
    <svg class="card-shapes" width="920" height="540" viewBox="0 0 920 540" aria-hidden="true">
      <path class="dark-panel" d="M610 0 C650 150 560 380 250 540 L920 540 L920 0 Z" fill="var(--panel-dark)"/>
      <path class="accent-swoosh" d="M582 0 L610 0 C650 150 560 380 250 540 C520 370 612 170 582 0 Z" fill="var(--accent-yellow)"/>
    </svg>

    <div class="brand">
      <div class="brand-square"></div>
      <div class="brand-name">
        <span class="word-main">Halvorsen</span>
        <span class="word-sub">Construction</span>
      </div>
    </div>

    <div class="person">
      <p class="person-name">Marcus Whitfield</p>
      <p class="person-title">Managing Director</p>
    </div>

    <address class="address">074.16th floor,Plaza<br>Quarry Road BKT</address>

    <ul class="contact-list">
      <li>012 345 6789
        <svg class="contact-icon" viewBox="0 0 24 24"><path fill="#fff" d="M6.6 10.8a15 15 0 0 0 6.6 6.6l2.2-2.2a1 1 0 0 1 1-.25 11.4 11.4 0 0 0 3.6.57 1 1 0 0 1 1 1V20a1 1 0 0 1-1 1A17 17 0 0 1 3 4a1 1 0 0 1 1-1h3.5a1 1 0 0 1 1 1c0 1.25.2 2.45.57 3.57a1 1 0 0 1-.25 1z"/></svg>
      </li>
      <li>012 345 6789
        <svg class="contact-icon" viewBox="0 0 24 24"><rect x="6" y="2" width="12" height="20" rx="2" fill="none" stroke="#fff" stroke-width="2"/><circle cx="12" cy="18" r="1.2" fill="#fff"/></svg>
      </li>
      <li>012 345 6789
        <svg class="contact-icon" viewBox="0 0 24 24"><rect x="7" y="3" width="10" height="6" fill="#fff"/><rect x="3" y="9" width="18" height="9" rx="1.5" fill="#fff"/><rect x="7" y="15" width="10" height="6" fill="#fff" stroke="#333" stroke-width="1"/></svg>
      </li>
      <li>urname@email.com
        <svg class="contact-icon" viewBox="0 0 24 24"><rect x="2" y="5" width="20" height="14" rx="1.5" fill="#fff"/><path d="M3 6l9 7 9-7" fill="none" stroke="#333" stroke-width="1.6"/></svg>
      </li>
      <li>www.urwebsitename.com
        <svg class="contact-icon" viewBox="0 0 24 24" fill="none" stroke="#fff" stroke-width="1.6"><circle cx="12" cy="12" r="9.5"/><ellipse cx="12" cy="12" rx="4" ry="9.5"/><path d="M2.5 12h19M4 7h16M4 17h16"/></svg>
      </li>
    </ul>
  </div>
</body>
</html>
```